Modern Dry eye Poster for eye center, Optometrist office

We need a banner to connect to patient about dry eye and treatment. Ask if patient has dry eyes and we offer treatment .
What is dry eye?
Are you suffering for dry, gritty, painful eyes, blurred vision, redness..

Now there is a quick, comfortable and affordable procedure offering relief tofdry eye.

Schedule your dry eye treatment today.

Target Market(s)

Dry eye patient

Font styles to use
Sans Serif

Colors
00a990
ffffff
0492cd
fbf289
85cae6

Requirements
Must have
• Modern design, dry eye patient
Nice to have
• real life model of nice eyes
Should not have
• No cartoon,

```html
<!DOCTYPE html>
<html lang="en">
<head>
<meta charset="utf-8">
<title>What Is Dry Eye – Brightlane Optometry</title>
<link rel="stylesheet" href="https://fonts.googleapis.com/css2?family=Montserrat:wght@300;400;500;600;700;800;900&display=swap">
<style>
  :root {
    --gold: #d6b338;
    --olive: #8a7014;
    --pine: #0e3b33;
    --blue: #0492cd;
    --ink: #222222;
    --slate: #5c5d61;
    --cream: #fdf6dc;
    --rule-gold: #e4c766;
    --band-gray: #c9cacc;
    --white: #ffffff;
  }
  * { margin: 0; padding: 0; box-sizing: border-box; }
  html, body {
    width: 900px; height: 1200px; overflow: hidden;
    background: var(--white);
    font-family: "Montserrat", Arial, sans-serif;
  }
  .poster {
    position: relative; width: 900px; height: 1200px; overflow: hidden;
    background: linear-gradient(180deg, var(--white) 0%, var(--white) 40%, var(--cream) 100%);
  }
  .model-photo {
    position: absolute; left: 0; top: 0; width: 640px; height: 1021px;
    background:
      linear-gradient(90deg, rgba(255,255,255,0) 0%, rgba(255,255,255,0) 55%, rgba(255,255,255,0.85) 85%, rgba(255,255,255,0) 100%),
      radial-gradient(ellipse at 30% 35%, #e9c9a8 0%, #e2b995 35%, #f3dcc6 65%, #fbf1e6 100%);
    -webkit-mask-image: linear-gradient(90deg, #000 0%, #000 70%, transparent 100%);
            mask-image: linear-gradient(90deg, #000 0%, #000 70%, transparent 100%);
  }
  .right { position: absolute; right: 29px; text-align: right; }
  .headline { line-height: 1; white-space: nowrap; }
  .headline-what { top: 32px; font-size: 160px; font-weight: 900; color: var(--gold); letter-spacing: -2px; }
  .headline-isdry { top: 158px; font-size: 114px; font-weight: 400; color: var(--pine); }
  .headline-eye { top: 254px; font-size: 172px; font-weight: 800; color: var(--blue); letter-spacing: -2px; }
  .rule { position: absolute; right: 46px; width: 100px; height: 1.5px; background: var(--rule-gold); }
  .rule-top { top: 428px; }
  .rule-mid { top: 656px; }
  .symptoms { top: 454px; line-height: 1.3; }
  .symptoms-lead { font-size: 25px; font-weight: 400; color: var(--ink); }
  .symptoms-list { font-size: 24px; font-weight: 600; color: var(--blue); }
  .symptoms-body { margin-top: 8px; font-size: 18px; font-weight: 400; color: var(--ink); line-height: 1.4; }
  .cta { top: 678px; line-height: 1; }
  .cta-lead { font-size: 34px; font-weight: 400; color: var(--ink); }
  .cta-main { margin-top: 6px; font-size: 84px; font-weight: 800; color: var(--blue); letter-spacing: -1px; }
  .cta-sub { margin-top: 2px; font-size: 40px; font-weight: 400; color: var(--ink); }
  .cta-sub strong { font-weight: 800; color: var(--olive); }
  .footer-band {
    position: absolute; left: 0; top: 1021px; width: 900px; height: 179px;
    background: var(--cream);
    border-top: 6px solid var(--band-gray);
  }
  .brand-card {
    position: absolute; left: 39px; top: 939px; width: 196px; height: 240px;
    background: var(--white);
    box-shadow: 0 0 8px rgba(0,0,0,0.08);
    display: flex; flex-direction: column; align-items: center; justify-content: center; gap: 22px;
  }
  .brand-square { width: 90px; height: 90px; background: var(--gold); }
  .brand-name { font-size: 19px; font-weight: 400; color: var(--slate); text-align: center; line-height: 1.15; letter-spacing: 1px; }
  .contact { top: 1036px; line-height: 1.35; }
  .contact-ask { font-size: 17px; font-weight: 400; color: var(--ink); }
  .contact-ask strong { font-weight: 600; color: var(--blue); }
  .contact-phone { margin-top: 10px; font-size: 62px; font-weight: 800; color: var(--slate); line-height: 1; letter-spacing: -1px; }
  .contact-web { margin-top: 4px; font-size: 17px; color: var(--ink); }
  .contact-web strong { font-size: 28px; font-weight: 700; color: var(--blue); }
</style>
</head>
<body>
<main class="poster">
  <div class="model-photo" role="img" aria-label="Portrait photograph of a woman touching her temple, skin around one eye shown dry and cracked"></div>

  <h1>
    <span class="right headline headline-what">WHAT</span>
    <span class="right headline headline-isdry">IS DRY</span>
    <span class="right headline headline-eye">EYE</span>
  </h1>

  <div class="rule rule-top"></div>

  <section class="right symptoms">
    <p class="symptoms-lead">Are You Suffering For</p>
    <p class="symptoms-list">Dry, Gritty, Painful Eyes,<br>Blurred Vision, Redness..</p>
    <p class="symptoms-body">Now there is a quick, comfortable<br>and affordable procedure offering<br>relief tofdry eye.</p>
  </section>

  <div class="rule rule-mid"></div>

  <section class="right cta">
    <p class="cta-lead">Schedule Your</p>
    <p class="cta-main">DRY EYE</p>
    <p class="cta-sub">TREATMENT <strong>TODAY</strong></p>
  </section>

  <div class="footer-band"></div>

  <div class="brand-card">
    <div class="brand-square"></div>
    <p class="brand-name">BRIGHTLANE<br>OPTOMETRY</p>
  </div>

  <section class="right contact">
    <p class="contact-ask">Ask for an <strong>Brightlane Optometry appointment</strong><br>at Reception Today</p>
    <p class="contact-phone">555-014-2210</p>
    <p class="contact-web">Visit Us at : <strong>www.brightlanesee.com</strong></p>
  </section>
</main>
</body>
</html>
```